Geschäftspapiere für medizinische Schutzausrüstung
Zielgruppe
Medizinische Schutzausrüstung für Deutschland.
Zertifiziert, schnell und unkompliziert.
Für Einrichtungen im Bereich Medizin & Pflege, systemrelevante Industrien sowie für öffentliche Träger.
Aufgabenstellung
Es sollte clean sein, Farben wie , Weiß, blau, grün, wären von Vorteil. Habe keine besondere Vorstellungen lasse mich gerne überraschen.
Siehe .. www.kvoltaq.de

```html
<!DOCTYPE html>
<html lang="de">
<head>
<meta charset="utf-8">
<title>Norvalen Schutztechnik – Briefbogen</title>
<link href="https://fonts.googleapis.com/css2?family=Lato:wght@400;700&display=swap" rel="stylesheet">
<style>
  :root {
    --backdrop: #e4e4e4;
    --paper: #ffffff;
    --sage: #8fae94;
    --navy: #1b2a45;
    --gold: #c9b35a;
    --muted: #7d7d7d;
    --fold: #6f8fb3;
  }
  * { margin: 0; padding: 0; box-sizing: border-box; }
  html, body { width: 1200px; height: 1105px; overflow: hidden; }
  body {
    background: var(--backdrop);
    font-family: "Lato", sans-serif;
    color: var(--navy);
  }
  .letterhead {
    position: absolute;
    left: 230px; top: 30px;
    width: 739px; height: 1045px;
    background: var(--paper);
    box-shadow: 0 6px 18px rgba(0,0,0,.18);
    overflow: hidden;
  }
  .band {
    position: absolute;
    height: 20px;
    background: var(--sage);
  }
  .band--top { top: 0; left: 0; width: 420px; border-bottom-right-radius: 14px; }
  .band--bottom { bottom: 0; right: 0; width: 407px; border-top-left-radius: 14px; }

  .brand {
    position: absolute; right: 40px; top: 148px;
    display: flex; align-items: center; gap: 10px;
  }
  .brand__dot { width: 14px; height: 14px; border-radius: 50%; background: var(--sage); }
  .brand__name {
    font-weight: 700; font-size: 17px; letter-spacing: .06em;
    text-transform: uppercase; color: var(--navy);
  }

  .sender-line {
    position: absolute; left: 84px; top: 196px;
    font-size: 9.5px; color: var(--muted);
    border-bottom: 1px solid var(--muted); padding-bottom: 2px;
  }
  .sender-line .sep { color: var(--fold); }

  .contact {
    position: absolute; left: 572px; top: 222px;
    padding-left: 16px; border-left: 1px solid var(--navy);
    font-size: 13px; line-height: 1.3; font-style: normal;
  }
  .contact__address { margin-bottom: 6px; }
  .contact__row { display: flex; align-items: center; gap: 8px; }
  .contact__row svg { width: 11px; height: 11px; flex: none; }

  .fold-mark {
    position: absolute; left: 0; width: 22px; height: 1px; background: var(--fold);
  }
  .fold-mark--1 { top: 370px; }
  .fold-mark--2 { top: 522px; }
  .fold-mark--3 { top: 739px; }

  .footer {
    position: absolute; top: 936px; left: 350px;
    display: flex; gap: 18px;
    font-size: 9.5px; color: var(--muted); line-height: 1.3;
  }
  .footer__bank { display: grid; grid-template-columns: 30px auto; column-gap: 6px; }
  .footer__divider { width: 1px; background: var(--muted); align-self: stretch; }
  .footer__register { display: grid; grid-template-columns: 64px auto; column-gap: 6px; align-self: flex-end; }
</style>
</head>
<body>
<main class="letterhead">
  <div class="band band--top" aria-hidden="true"></div>

  <div class="brand">
    <span class="brand__dot"></span>
    <span class="brand__name">Norvalen Schutztechnik</span>
  </div>

  <p class="sender-line">Kellmannweg 17 <span class="sep">•</span> 30421 Hannover</p>

  <address class="contact">
    <div class="contact__address">Rosmarstraße 12<br>31188 Hildesheim</div>
    <div class="contact__row">
      <svg viewBox="0 0 12 12"><path d="M2 1 L4.5 1 L5.5 4 L4 5 Q5 7.5 7 8 L8 6.5 L11 7.5 L11 10 Q6 11 2.5 7 Q1 4 2 1Z" fill="var(--gold)"/></svg>
      <span>05121 48302</span>
    </div>
    <div class="contact__row">
      <svg viewBox="0 0 12 12"><rect x="1" y="4" width="10" height="6" rx="1" fill="none" stroke="var(--gold)"/><rect x="3" y="1.5" width="6" height="3" fill="none" stroke="var(--gold)"/></svg>
      <span>05121 48309</span>
    </div>
    <div class="contact__row">
      <svg viewBox="0 0 12 12"><circle cx="6" cy="6" r="4.8" fill="none" stroke="var(--gold)"/><path d="M1.2 6H10.8M6 1.2Q3.5 6 6 10.8M6 1.2Q8.5 6 6 10.8" fill="none" stroke="var(--gold)" stroke-width=".8"/></svg>
      <span>www.norvalen.de</span>
    </div>
    <div class="contact__row">
      <svg viewBox="0 0 12 12"><rect x="1" y="2.5" width="10" height="7" fill="none" stroke="var(--gold)"/><path d="M1 2.5 L6 6.5 L11 2.5" fill="none" stroke="var(--gold)"/></svg>
      <span>info@norvalen.de</span>
    </div>
  </address>

  <span class="fold-mark fold-mark--1"></span>
  <span class="fold-mark fold-mark--2"></span>
  <span class="fold-mark fold-mark--3"></span>

  <footer class="footer">
    <div class="footer__bank">
      <span>Bank:</span><span>Leinetaler Kontorbank eG<br>Hildesheim-Sarstedt</span>
      <span>BIC</span><span>LKTBDE21HIL</span>
      <span>IBAN</span><span>DE41 2517 4422 0846 3317 00</span>
    </div>
    <span class="footer__divider"></span>
    <div class="footer__register">
      <span>USt-IdNr.:</span><span>DE381529604</span>
      <span>Register-Nr.</span><span>HRA 3187</span>
    </div>
  </footer>

  <div class="band band--bottom" aria-hidden="true"></div>
</main>
</body>
</html>
```